Etiketten-Design für Trinkweine
Zielgruppe
Wir sind eine Weinkellerei, die einfache Trinkweine für den LEH herstellt.
Unsere Zielgruppen sind Jugendliche .
Wir suchen ein Etikett für unser neues Produkt ,,Traubensaftschorle`` alkoholfrei
Aufgabenstellung
Siehe Anhang , eigene ideen sind auch erwünscht.
Das Etikett sollte Natur verbunden wirken da es ein Bio Produkt ist.
Farben: weiß, grün wären erwünscht.
Das Etikett sollte 75mm hoch und 120mm Breit sein
Strukturpapier weiß
Anbei auch unserer Standartetikett gerne kann das Logo übernommen werden

```html
<!DOCTYPE html>
<html lang="de">
<head>
<meta charset="utf-8">
<title>Traubensaftschorle – Etikett</title>
<link href="https://fonts.googleapis.com/css2?family=Amatic+SC:wght@700&family=Nunito+Sans:wght@300;400&display=swap" rel="stylesheet">
<style>
  :root {
    --page-bg: #e8ebe3;
    --cream: #fdf4e8;
    --cream-deep: #f3e8d4;
    --sage: #9bb79b;
    --sage-deep: #8aab8a;
    --forest: #2f6a35;
    --ink: #111111;
    --white: #ffffff;
  }
  * { margin: 0; padding: 0; box-sizing: border-box; }
  html, body { width: 1200px; height: 1200px; overflow: hidden; background: var(--page-bg); }
  .canvas { position: relative; width: 1200px; height: 1200px; }

  .label {
    position: absolute; left: 40px; top: 250px;
    width: 1120px; height: 700px;
    display: flex;
    box-shadow: 0 8px 30px rgba(40, 60, 40, .18);
  }

  /* front panel */
  .front { position: relative; width: 566px; height: 100%; }
  .front-pattern {
    position: absolute; inset: 0;
    background: radial-gradient(circle at 50% 50%, var(--cream) 35%, var(--cream-deep) 100%);
  }
  .front-ring { position: absolute; left: 0; top: 0; }
  .brand-name {
    position: absolute; top: 30px; left: 0; width: 100%;
    text-align: center;
    font-family: "Amatic SC", cursive;
    font-weight: 700; font-size: 48px; color: var(--ink);
    line-height: 1;
  }
  .product-title {
    position: absolute; left: 0; width: 100%; top: 210px;
    text-align: center;
    font-family: "Amatic SC", cursive;
    font-weight: 700; font-size: 112px; line-height: 92px;
    color: var(--ink);
    letter-spacing: 1px;
  }
  .volume {
    position: absolute; left: 50%; top: 648px;
    transform: translateX(-50%);
    width: 92px; height: 46px; border-radius: 50%;
    background: var(--white);
    display: flex; align-items: center; justify-content: center;
    font-family: "Amatic SC", cursive; font-weight: 700; font-size: 34px;
    color: var(--ink);
  }

  /* back panel */
  .back { position: relative; flex: 1; height: 100%; }
  .back-pattern {
    position: absolute; inset: 0;
    background: linear-gradient(160deg, var(--sage) 0%, var(--sage-deep) 100%);
  }
  .info-card {
    position: absolute; left: 72px; top: 94px;
    width: 412px; height: 516px;
    background: var(--white); border-radius: 22px;
    padding: 14px;
  }
  .info-frame {
    width: 100%; height: 100%;
    border: 1.5px solid var(--forest); border-radius: 16px;
    font-family: "Nunito Sans", sans-serif; font-weight: 300;
    font-size: 30px; line-height: 40px; color: var(--ink);
    text-align: center;
    padding-top: 60px;
  }
  .info-desc { margin-bottom: 68px; }
  .info-lot { margin-bottom: 56px; }
</style>
</head>
<body>
<div class="canvas">
  <div class="label">
    <section class="front">
      <div class="front-pattern" role="img" aria-label="Ornamentmuster aus Ranken, Blättern und Trauben in Salbeigrün auf Creme"></div>
      <svg class="front-ring" width="566" height="700" viewBox="0 0 566 700" aria-hidden="true">
        <ellipse cx="282" cy="350" rx="190" ry="192" fill="var(--cream)" stroke="var(--forest)" stroke-width="2.5" stroke-dasharray="16 11"/>
      </svg>
      <div class="brand-name">Petra Finkel</div>
      <h1 class="product-title">Trauben<br>Saft<br>Schorle</h1>
      <div class="volume">0,33 L</div>
    </section>
    <section class="back">
      <div class="back-pattern" role="img" aria-label="Ornamentmuster aus Ranken, Blättern und Trauben in Weiß auf Salbeigrün"></div>
      <div class="info-card">
        <div class="info-frame">
          <p class="info-desc">Trauben saft&nbsp; mit<br>zugestlew kohlensäure</p>
          <p class="info-lot">VOS Nr. 01/20</p>
          <p class="info-bottler">Abfüller: Petra Finkel<br>Lindenweg 14<br>79312 Sonnbach</p>
        </div>
      </div>
    </section>
  </div>
</div>
</body>
</html>
```